Storm Restoration Contractor needs a professional business card design

Looking for a professional business card design. Not looking for your cheapo MS Word standard ones that are readily available. Dont want it to be cookie cutter look like ones readily available online. We just recently changed our logo and want to freshen up all our documents. Our company handles restoring a property back to a pre-loss condition after a storm damages it. For example, wind, hail, flood, fire losses.

Target Market(s)

Property Owners, Homeowners, Property Owners, Commercial Property Owners, Property Management Companies, Hail and Wind Damaged Properties

Industry/Entity Type

Construction Company

Contact Information for Business Card

Brightline Facades
847-555-0193
847-555-0147 fax
www.brightlinefacades.example
info@brightlinefacades.example

Requirements
Must have
• Clean, Professional, fresh look
• Storm Restoration, Roofing, Siding, Windows
Nice to have
• If there is a way to incorporate storms that may be cool.

```html
<!DOCTYPE html>
<html lang="en">
<head>
<meta charset="utf-8">
<title>Brightline Facades — Business Card</title>
<link href="https://fonts.googleapis.com/css2?family=Oswald:wght@500;600&family=Open+Sans:wght@400&display=swap" rel="stylesheet">
<style>
  :root {
    --bg-center: #b9b9b9;
    --bg-edge: #7a7a7a;
    --card: #1f1f20;
    --card-edge: #2a2a2b;
    --silver: #c9cacc;
    --white: #f4f4f4;
    --text-soft: #bfbfbf;
    --blue: #2f86d6;
    --divider: #5a5a5c;
  }
  * { box-sizing: border-box; margin: 0; padding: 0; }
  html, body { width: 1200px; height: 1000px; overflow: hidden; }
  body {
    background: radial-gradient(ellipse at 50% 45%, var(--bg-center) 0%, var(--bg-edge) 80%);
    position: relative;
    font-family: "Open Sans", sans-serif;
  }
  .card {
    position: absolute;
    width: 560px;
    height: 330px;
    border-radius: 26px;
    background: linear-gradient(160deg, var(--card-edge), var(--card));
    box-shadow: 0 18px 40px rgba(0,0,0,.35);
    overflow: hidden;
  }
  /* Front */
  .card-front { left: 70px; top: 110px; }
  .front-brand {
    position: absolute; inset: 0;
    display: flex; align-items: center; justify-content: center; gap: 26px;
  }
  .brand-circle {
    width: 96px; height: 96px; border-radius: 50%;
    border: 3px solid #141414;
    box-shadow: inset 0 0 0 1px #303031;
  }
  .brand-divider { width: 1px; height: 120px; background: var(--divider); }
  .brand-name {
    font-family: "Oswald", sans-serif; font-weight: 600;
    color: var(--silver); font-size: 50px; line-height: 1.02;
    letter-spacing: 3px; text-transform: uppercase;
  }
  /* Back */
  .card-back { left: 570px; top: 520px; }
  .back-identity {
    position: absolute; left: 20px; top: 92px; width: 256px; text-align: right;
  }
  .back-name {
    font-family: "Oswald", sans-serif; font-weight: 500;
    color: var(--white); font-size: 25px; letter-spacing: 1px; text-transform: uppercase;
    white-space: nowrap; line-height: 1.2;
  }
  .back-title {
    font-family: "Open Sans", sans-serif; color: var(--blue); font-size: 18px; line-height: 1.1;
  }
  .back-divider {
    position: absolute; left: 292px; top: 66px; width: 1px; height: 104px; background: var(--divider);
  }
  .contact-list {
    position: absolute; left: 306px; top: 66px; list-style: none;
  }
  .contact-list li {
    display: flex; align-items: center; gap: 11px;
    color: var(--text-soft); font-size: 13.5px; line-height: 25px; white-space: nowrap;
  }
  .contact-list svg, .address svg { width: 12px; height: 12px; fill: var(--blue); flex: none; }
  .accent { color: var(--blue); }
  .address {
    position: absolute; left: 150px; bottom: 50px;
    display: flex; align-items: center; gap: 10px;
    color: var(--text-soft); font-size: 15px; white-space: nowrap;
  }
  .address svg { width: 13px; height: 16px; }
</style>
</head>
<body>
  <section class="card card-front" aria-label="Card front">
    <div class="front-brand">
      <div class="brand-circle"></div>
      <div class="brand-divider"></div>
      <div class="brand-name">Brightline<br>Facades</div>
    </div>
  </section>

  <section class="card card-back" aria-label="Card back">
    <div class="back-identity">
      <div class="back-name">Brightline Facades</div>
      <div class="back-title">CEO</div>
    </div>
    <div class="back-divider"></div>
    <ul class="contact-list">
      <li><svg viewBox="0 0 24 24"><path d="M6.6 10.8a15 15 0 0 0 6.6 6.6l2.2-2.2a1 1 0 0 1 1-.25 11.4 11.4 0 0 0 3.6.57 1 1 0 0 1 1 1V20a1 1 0 0 1-1 1A17 17 0 0 1 3 4a1 1 0 0 1 1-1h3.5a1 1 0 0 1 1 1c0 1.25.2 2.45.57 3.57a1 1 0 0 1-.25 1z"/></svg><span>847-555-0193</span></li>
      <li><svg viewBox="0 0 24 24"><path d="M6 2h9l3 3v5H6zM3 11h18a1 1 0 0 1 1 1v8a1 1 0 0 1-1 1H3a1 1 0 0 1-1-1v-8a1 1 0 0 1 1-1zm3 3v2h12v-2z"/></svg><span>847-555-0147</span></li>
      <li><svg viewBox="0 0 24 24"><path d="M2 5h20v14H2zm2 2v.5l8 5 8-5V7l-8 5z"/></svg><span>info@brightlinefacades.example</span></li>
      <li><svg viewBox="0 0 24 24"><path d="M12 2a10 10 0 1 0 0 20 10 10 0 0 0 0-20zm6.9 9h-3a15 15 0 0 0-1.3-5.6A8 8 0 0 1 18.9 11zM12 4.1c.9 1.2 1.7 3.5 1.9 6.9h-3.8c.2-3.4 1-5.7 1.9-6.9zM9.4 5.4A15 15 0 0 0 8.1 11h-3a8 8 0 0 1 4.3-5.6zM5.1 13h3a15 15 0 0 0 1.3 5.6A8 8 0 0 1 5.1 13zm6.9 6.9c-.9-1.2-1.7-3.5-1.9-6.9h3.8c-.2 3.4-1 5.7-1.9 6.9zm2.6-1.3a15 15 0 0 0 1.3-5.6h3a8 8 0 0 1-4.3 5.6z"/></svg><span>www.<span class="accent">brightlinefacades</span>.example</span></li>
    </ul>
    <div class="address">
      <svg viewBox="0 0 20 26"><path d="M10 0a10 10 0 0 0-10 10c0 7 10 16 10 16s10-9 10-16A10 10 0 0 0 10 0zm0 14a4 4 0 1 1 0-8 4 4 0 0 1 0 8z"/></svg>
      <span>Your Street Address, Singapore, 1234</span>
    </div>
  </section>
</body>
</html>
```